Brightmoor Academy - Personal Development business 2.0 needs a social post format design.

https://www.brightmooracademy.example

Our focus with Brightmoor Academy is on developing people through knowledge and skills to improve their everyday lives.
We love simplicity, Quorel design and less is more.

We are crazy about personal growth, science, design, the latest gadgets and people.

We need 4 formats for our social media posts.
1. Blogs -to pronounce a blog post
2. Workshop /training - to pronounce our workshops/trainings (both online and offline)
3. Podcast - called "Wissel je blik". To pronounce a guest we've spoken. The host is called Berend.
4. Facts - to pronounce short facts about personal development. Invites people to read more.
The formats should include: high quality pictogram (better than the uploaded picto's), 1 of the 3 logo's in the design.
It's important that we can edit the design in Lumora Draw / Lumora Pixel to adjust the text in the format.

Attached you find four of our current designs, which are a poor example of how the designs should look like. These are just to show you how much lines of text (more or less) will be in the designs. So please do not make a design that looks like these ;) You have carte blanche.

Our customers are mostly women (80%). We focus on both business and casual customers.

Target Market(s)

80% woman, 20% men. We focus on both business and casual customers.

Requirements
Must have
• Less is more. Quorel Design alike. Simplicity.
Aimed at the women target audience.
Designs must be edible for adjusting the text in the format.
Nice to have
• Unique concept.
The design should "breathe".
Each design can have a different color, so customers identify the specific post with specific information. For example, blog is red, workshop post black, etc.

```html
<!DOCTYPE html>
<html lang="nl">
<head>
<meta charset="utf-8">
<title>Brightmoor Academy – social post formats</title>
<link href="https://fonts.googleapis.com/css2?family=Signika:wght@400;600;700&display=swap" rel="stylesheet">
<style>
  :root {
    --canvas: #ebebeb;
    --text: #ffffff;
    --text-soft: rgba(255, 255, 255, 0.78);
    --workshop: #242323;
    --workshop-band: #3f4343;
    --photo-light: #707070;
    --photo-dark: #333333;
    --blog: #b65a50;
    --blog-band: #c7756b;
    --podcast: #5a3d5c;
    --podcast-band: #6e4f70;
    --facts: #6f8d79;
    --facts-band: #86a28f;
  }
  * { box-sizing: border-box; margin: 0; padding: 0; }
  html, body { width: 1200px; height: 600px; overflow: hidden; }
  body {
    background: var(--canvas);
    font-family: "Signika", Arial, sans-serif;
    color: var(--text);
    position: relative;
  }

  .post {
    position: absolute;
    top: 165px;
    width: 271px;
    height: 271px;
    overflow: hidden;
  }
  .post--workshop { left: 20px;  background: var(--workshop); }
  .post--blog     { left: 316px; background: var(--blog); }
  .post--podcast  { left: 613px; background: var(--podcast); }
  .post--facts    { left: 909px; background: var(--facts); }

  .post__band { position: absolute; inset: 0; width: 100%; height: 100%; }

  .brand {
    position: absolute;
    left: 22px;
    top: 22px;
    font-size: 11px;
    font-weight: 600;
    display: flex;
    align-items: center;
    gap: 5px;
  }
  .brand__dot { width: 6px; height: 6px; border-radius: 50%; background: var(--text); }

  .category {
    position: absolute;
    right: 22px;
    top: 18px;
    display: flex;
    align-items: center;
    gap: 6px;
    font-size: 10px;
    font-weight: 600;
    letter-spacing: 1.2px;
    text-transform: uppercase;
  }
  .category svg { width: 22px; height: 22px; }

  .headline {
    position: absolute;
    left: 22px;
    right: 22px;
    top: 92px;
    font-size: 21px;
    line-height: 23px;
    font-weight: 700;
  }
  .body {
    position: absolute;
    left: 22px;
    right: 22px;
    font-size: 11.5px;
    line-height: 16px;
    font-weight: 400;
    color: var(--text-soft);
  }
  .cta {
    position: absolute;
    left: 22px;
    bottom: 22px;
    font-size: 11px;
    font-weight: 600;
    padding-bottom: 3px;
    border-bottom: 1.5px solid var(--text);
  }

  /* workshop */
  .photo {
    position: absolute;
    right: 0;
    top: 0;
    width: 118px;
    height: 100%;
    background: linear-gradient(160deg, var(--photo-light), var(--photo-dark));
  }
  .post--workshop .category { right: 140px; }
  .post--workshop .headline { right: 140px; text-transform: uppercase; line-height: 22px; }
  .post--workshop .body { top: 170px; right: 140px; }
</style>
</head>
<body>

  <section class="post post--workshop">
    <div class="photo" role="img" aria-label="Zwart-witportret van de trainer"></div>
    <div class="brand"><span class="brand__dot"></span>Brightmoor Academy</div>
    <h2 class="headline">Pre-New<br>Year’s Eve</h2>
    <p class="body">Dinsdag 29 dec<br>19–21u<br>Online training</p>
    <span class="cta">Meld je aan</span>
  </section>

  <section class="post post--blog">
    <svg class="post__band" viewBox="0 0 271 271" aria-hidden="true">
      <path d="M0,230 Q150,205 271,150 L271,175 Q150,235 0,250 Z" fill="var(--blog-band)"/>
    </svg>
    <div class="brand"><span class="brand__dot"></span>Brightmoor Academy</div>
    <h2 class="headline">De beste manier om je voor te bereiden op 2021!</h2>
    <p class="body" style="top:170px">Nieuw op de blog</p>
    <span class="cta">Lees de blog →</span>
  </section>

  <section class="post post--podcast">
    <svg class="post__band" viewBox="0 0 271 271" aria-hidden="true">
      <path d="M0,230 Q150,205 271,150 L271,175 Q150,235 0,250 Z" fill="var(--podcast-band)"/>
    </svg>
    <div class="brand"><span class="brand__dot"></span>Brightmoor Academy</div>
    <h2 class="headline">Wissel je blik</h2>
    <p class="body" style="top:122px">Berend in gesprek over de 3<br>belangrijkste tools voor 2021</p>
    <span class="cta">Luister nu →</span>
  </section>

  <section class="post post--facts">
    <svg class="post__band" viewBox="0 0 271 271" aria-hidden="true">
      <path d="M0,230 Q150,205 271,150 L271,175 Q150,235 0,250 Z" fill="var(--facts-band)"/>
    </svg>
    <div class="brand"><span class="brand__dot"></span>Brightmoor Academy</div>
    <h2 class="headline">2 uur per week leren maakt al verschil.</h2>
    <p class="body" style="top:170px">Wist je dat?</p>
    <span class="cta">brightmooracademy.example/event</span>
  </section>

</body>
</html>
```